Business Card Design for Kidvale (Hires out childrens play areas)

Looking to have a business card designed for a company we just bought. The company rents out childrens play areas.

I have uploaded a couple of examples of the kind of business card style I like. Here are two more examples:

https://quorvastudio.nz/project/bright-romp-branding/
https://imgvaultcdn.com/design_img/8841052/302917/302917_5518203_8841052_b73e19a2_image.jpg

I think a white card will be best due to all the colours in the logo.

Size we require: 3.75" x 2.25" (horizontally orientated) with a 0.125" bleed

Uploaded is two versions of our logo.

Details for the card:
1. My name: Liam Verster
2. Title: Managing Director
3. Phone no: 021 563 417
4. Email: liam@kidvale.co.nz
5. URL: www.kidvale.co.nz
6. Address:
PO Box 318625
Fernlea, Auckland

Let me know if you need anything else.

Target Market(s)

Hospitals, doctors surgeries, bed shops, etc.

Contact Information for Business Card

Details for the card:
1. My name: Liam Verster
3. Phone no: 021 563 417
5. URL: www.kidvale.co.nz
6. Address:
PO Box 318625
Fernlea, Auckland

Requirements
Should not have
• Not too busy.

```html
<!DOCTYPE html>
<html lang="en">
<head>
<meta charset="utf-8">
<title>Kidvale Business Card</title>
<link rel="stylesheet" href="https://fonts.googleapis.com/css2?family=Lato:wght@400;700;900&display=swap">
<style>
  :root {
    --stage: #1b1b1d;
    --purple: #7a3189;
    --orange: #f5a81c;
    --white: #ffffff;
    --card-w: 640px;
    --card-h: 384px;
  }
  * { margin: 0; padding: 0; box-sizing: border-box; }
  html, body {
    width: 1200px;
    height: 912px;
    overflow: hidden;
    background: var(--stage);
    font-family: "Lato", sans-serif;
  }
  .sheet {
    position: relative;
    width: 1200px;
    height: 912px;
  }
  .card {
    position: absolute;
    width: var(--card-w);
    height: var(--card-h);
    background: var(--purple);
    overflow: hidden;
  }
  .card--front { left: 180px; top: 56px; }
  .card--back  { left: 380px; top: 472px; }

  .brand {
    display: flex;
    align-items: center;
    gap: 12px;
    font-weight: 900;
    letter-spacing: 0.5px;
  }
  .brand__dot {
    width: 22px;
    height: 22px;
    border-radius: 50%;
    background: var(--orange);
  }
  .card--front .brand {
    position: absolute;
    left: 0; right: 0;
    top: 130px;
    justify-content: center;
    font-size: 58px;
    color: var(--white);
  }
  .card--front .front-url {
    position: absolute;
    left: 0; right: 0;
    top: 258px;
    text-align: center;
    color: var(--white);
    font-size: 17px;
    letter-spacing: 0.3px;
  }

  .back-art { position: absolute; inset: 0; }
  .card--back .brand {
    position: absolute;
    left: 380px;
    top: 118px;
    font-size: 50px;
    color: var(--purple);
  }
  .details {
    position: absolute;
    left: 48px;
    top: 128px;
    color: var(--white);
  }
  .details__name {
    color: var(--orange);
    font-weight: 700;
    font-size: 25px;
    line-height: 1.1;
  }
  .details__title {
    font-size: 17px;
    margin-top: 2px;
  }
  .details__address {
    font-size: 17px;
    line-height: 1.3;
    margin-top: 22px;
  }
  .contact {
    list-style: none;
    margin-top: 20px;
  }
  .contact__item {
    display: flex;
    align-items: center;
    gap: 12px;
    font-size: 17px;
    line-height: 1.45;
  }
  .contact__icon {
    width: 15px;
    height: 15px;
    flex: none;
  }
</style>
</head>
<body>
<main class="sheet">

  <section class="card card--front" aria-label="Card front">
    <div class="brand"><span class="brand__dot"></span><span>Kidvale</span></div>
    <p class="front-url">www.kidvale.co.nz</p>
  </section>

  <section class="card card--back" aria-label="Card back">
    <svg class="back-art" viewBox="0 0 640 384" width="640" height="384" aria-hidden="true">
      <path d="M250 0 C255 245 450 378 640 352 L640 0 Z" fill="var(--orange)"/>
      <path d="M272 0 C278 236 458 364 640 342 L640 0 Z" fill="var(--purple)"/>
      <path d="M284 0 C290 230 464 354 640 336 L640 0 Z" fill="var(--orange)"/>
      <path d="M296 0 C300 224 470 346 640 330 L640 0 Z" fill="var(--white)"/>
    </svg>

    <div class="brand"><span class="brand__dot"></span><span>Kidvale</span></div>

    <div class="details">
      <h1 class="details__name">Liam Verster</h1>
      <p class="details__title">Managing Director</p>
      <p class="details__address">PO Box 318625<br>Fernlea, Auckland</p>
      <ul class="contact">
        <li class="contact__item">
          <svg class="contact__icon" viewBox="0 0 16 16" aria-hidden="true"><path d="M3 1 L6 1 L7 5 L5 6.5 C6 9 7 10 9.5 11 L11 9 L15 10 L15 13 C15 14 14 15 13 15 C6 15 1 10 1 3 C1 2 2 1 3 1 Z" fill="var(--orange)"/></svg>
          <span>021 563 417</span>
        </li>
        <li class="contact__item">
          <svg class="contact__icon" viewBox="0 0 16 16" aria-hidden="true"><rect x="1" y="3" width="14" height="10" fill="var(--orange)"/><path d="M1 3 L8 9 L15 3" fill="none" stroke="var(--purple)" stroke-width="1.4"/></svg>
          <span>liam@kidvale.co.nz</span>
        </li>
        <li class="contact__item">
          <svg class="contact__icon" viewBox="0 0 16 16" aria-hidden="true"><circle cx="8" cy="8" r="7" fill="var(--orange)"/><g fill="none" stroke="var(--purple)" stroke-width="1"><ellipse cx="8" cy="8" rx="3" ry="7"/><path d="M1 8 H15 M2.5 4.5 H13.5 M2.5 11.5 H13.5"/></g></svg>
          <span>www.kidvale.co.nz</span>
        </li>
      </ul>
    </div>
  </section>

</main>
</body>
</html>
```